Hostlane EOFYS Banner Ad Design Project

We're launching an End of Financial Year Sale for full-year paying customers to receive 6 bonus/extra months for free. We'd like to have two banners (both the same, but slightly adjusted for size) created that draw in customers.

Ideally, working within our colour scheme is ideal, but if you have ideas that you think will work, please don't hesitate to submit these ideas.

Target Market(s)

web developers, IT professionals, web designers, Australian medium to enterprise businesses

Industry/Entity Type

Financial

Requirements
Must have
• Two sizes:
#1: width="824" height="193"
#2: width="997" height="234"

Must have promotion code "qrtvm2013"
Must be provided source files (i.e. PSD, AI, EPS etc) as well as JPG/PNG finals.

"EOFYS" or "E.O.F.Y.S."

"Get 18 months for the price of 12!" or "Pre-pay 12 months, get a BONUS 6 MONTHS FREE." (capitalisation at your discretion)
Nice to have
• Hostlane colours (red (cc0000, 204 parts red, no blue or green), black and white; optional 85% grey).

A fitting "look and feel" reflective of Hostlane's corporate image (see www.hostlane.com.au or www.facebook.com/HostlaneAU for some ideas/inspiration of what has been accepted before).
Should not have
• No variations of the Hostlane logo (if used).

```html
<!DOCTYPE html>
<html lang="en">
<head>
<meta charset="utf-8">
<title>Hostlane EOFYS Banner</title>
<link rel="stylesheet" href="https://fonts.googleapis.com/css2?family=Titillium+Web:wght@400;600;700&display=swap">
<style>
  :root {
    --page: #ffffff;
    --ink: #000000;
    --white: #ffffff;
    --brand-red: #cc0000;
    --shade-dark: #0a0101;
    --shade-red: #4a0709;
    --shade-bright: #6e0a0d;
    --shade-grey: #1c1a1a;
  }
  html, body {
    margin: 0;
    padding: 0;
    width: 1200px;
    height: 1000px;
    overflow: hidden;
    background: var(--page);
    font-family: "Titillium Web", sans-serif;
  }
  .banner {
    position: absolute;
    left: 102px;
    top: 383px;
    width: 997px;
    height: 234px;
    overflow: hidden;
    background: var(--ink);
  }
  .banner-backdrop {
    position: absolute;
    inset: 0;
    background: linear-gradient(90deg,
      var(--ink) 0%,
      var(--shade-dark) 12%,
      var(--shade-red) 35%,
      var(--shade-bright) 58%,
      var(--shade-grey) 76%,
      var(--ink) 92%);
  }
  .headline {
    position: absolute;
    left: 48px;
    top: 28px;
    margin: 0;
    color: var(--white);
    font-size: 35px;
    font-weight: 600;
    line-height: 1;
  }
  .offer {
    position: absolute;
    left: 48px;
    top: 83px;
    margin: 0;
    color: var(--white);
    font-size: 28.7px;
    font-weight: 400;
    line-height: 31px;
  }
  .offer strong { font-weight: 700; }
  .promo-tag {
    position: absolute;
    left: 375px;
    top: 142px;
    width: 110px;
    height: 54px;
    background: var(--white);
    border-radius: 10px;
    text-align: center;
    box-sizing: border-box;
    padding-top: 8px;
  }
  .promo-label {
    display: block;
    color: var(--ink);
    font-size: 14.5px;
    line-height: 15px;
  }
  .promo-code {
    display: block;
    color: var(--brand-red);
    font-size: 20px;
    font-weight: 600;
    line-height: 22px;
  }
</style>
</head>
<body>
  <section class="banner">
    <div class="banner-backdrop" role="img" aria-label="Abstract flowing red, black and silver ribbon artwork"></div>
    <h1 class="headline">EOFYS</h1>
    <p class="offer">Pre-pay 12 months and get a Bonus<br>6 months for <strong>FREE</strong></p>
    <div class="promo-tag">
      <span class="promo-label">Promotion code</span>
      <span class="promo-code">qrtvm2013</span>
    </div>
  </section>
</body>
</html>
```